Business Name: MT Property Styling Pty Ltd

Business Type: Professional Home Styling and Minor Renovation Business

Logo: Attached is the logo that has been created.
I always envisaged the logo in the middle of the business card with my full name underneath it.

Maren Tulloch B.Com RVA DMH
Property Stylist & Project Manager

Include dot points of services
Staging Houses for Sale
Minor Home Renovations
Home Styling & Project Management
Re-Designing Living Spaces to Aid the Disabled

Somewhere on the card I would like to incorporate
"Property Styling and Cosmetic Renovations"

Colour Scheme:
Gloss black business card, with white and then
Gold or Silver as the highlight colours.

Incorporate a small amount of yellow only if possible to make it pop. If this really doesn’t work it doesn’t have to be used. Also l like the colour teal if that needs to be used as a contrast colour.

Feel/Themes
• I love antique chairs, regal expensive looking furniture mixed with modern homes (this is the unique style I want to sell) antique and modern mix that looks high class as well as modern and fresh, targeting an executive market.
• I want to use an orchid as a trademark throughout the course of my work, not sure if this can somehow be incorporated? Also really like crowns to give that regal/antique feel and then something else to give that modern twist (I don’t know what the something else could be)
• Wall Paper Look (on a portion of it not all of it, like a French look)
• Overall feel - A very deluxe and professional feel with a little bit of creative flare.

I hope this helps create a bit of a picture.

Is it ok that I call you tomorrow morning? My mobile number is 0491 862 574 if you have any questions for me in the meantime.

Target Market(s)

High Quality Executive Market - People selling homes

Industry/Entity Type

Business

Contact Information for Business Card

Include dot points of services:
Staging Houses for Sale
Minor Home Renovations

Font styles to use
Serif
Script

Colors
33b8a4
fbed22

Requirements
Must have
• Maren Tulloch B.Com RVA DMH
• Property Stylist & Project Manager
• RVA and DMH Logos on the card
• "Dramatically increase the value of your property"
Nice to have
• Colour Scheme:
• Gloss black business card, with white and then
• Gold or Silver as the highlight colours.
• Incorporate a small amount of yellow only if possible to make it pop. If this really doesn’t work it doesn’t have to be used. Also l like the colour teal if that needs to be used as a contrast colour.
• Also like teal as a highlight colour.

```html
<!DOCTYPE html>
<html lang="en">
<head>
<meta charset="utf-8">
<title>MT Property Styling Pty Ltd — Business Card</title>
<link rel="stylesheet" href="https://fonts.googleapis.com/css2?family=Cinzel:wght@400;600&family=Cormorant+Garamond:wght@400;500&display=swap">
<style>
  :root {
    --backdrop: #ffffff;
    --card-black: #0c0c0c;
    --card-charcoal: #232323;
    --gold: #c9a13c;
    --gold-light: #e8c766;
    --gold-deep: #8a6a1f;
    --silver: #b9b9b9;
    --text-soft: #d2d2d2;
  }
  * { box-sizing: border-box; margin: 0; padding: 0; }
  html, body {
    width: 1200px; height: 900px; overflow: hidden;
    background: var(--backdrop);
  }
  .canvas {
    position: relative; width: 1200px; height: 900px;
    display: flex; justify-content: center; align-items: center; gap: 36px;
  }
  .card {
    position: relative; width: 540px; height: 310px; border-radius: 24px;
    overflow: hidden;
  }

  /* Back of card */
  .card--back {
    background: radial-gradient(ellipse at 55% 40%, var(--card-charcoal) 0%, var(--card-black) 70%);
    font-family: "Cormorant Garamond", Georgia, serif;
    color: var(--text-soft);
  }
  .services {
    list-style: none; position: absolute; left: 28px; top: 30px;
    font-size: 19px; line-height: 30px;
  }
  .services li::before {
    content: ""; display: inline-block; width: 5px; height: 5px; border-radius: 50%;
    background: var(--gold-light); margin-right: 8px; vertical-align: middle;
  }
  .contact {
    list-style: none; position: absolute; left: 28px; top: 176px;
    font-size: 15px; line-height: 19.5px;
  }
  .contact li { display: flex; align-items: center; gap: 4px; }
  .contact svg { width: 12px; height: 12px; flex: none; }

  /* Front of card */
  .card--front {
    background: var(--gold);
    background: linear-gradient(135deg, var(--gold-light), var(--gold-deep) 45%, var(--gold-light) 75%, var(--gold-deep));
    padding: 6px;
  }
  .card__face {
    position: relative; width: 100%; height: 100%; border-radius: 19px;
    background: var(--card-black); overflow: hidden;
    display: flex; flex-direction: column; align-items: center;
  }
  .wallpaper {
    position: absolute; inset: 0;
    background: radial-gradient(ellipse at 50% 45%, #2e2e2e 0%, #161616 60%, #0b0b0b 100%);
  }
  .tagline {
    position: relative; margin-top: 20px;
    font-family: "Cinzel", Georgia, serif; font-size: 11.5px; letter-spacing: 2.4px;
    color: var(--silver);
  }
  .brand-name {
    position: relative; margin-top: 88px;
    font-family: "Cinzel", Georgia, serif; font-weight: 600; font-size: 22px;
    letter-spacing: 1.5px; color: var(--gold);
  }
  .holder {
    position: relative; margin-top: 72px; text-align: center;
    font-family: "Cinzel", Georgia, serif; color: var(--gold);
  }
  .holder__name { font-size: 15.5px; letter-spacing: 0.5px; }
  .holder__role { font-size: 9.5px; letter-spacing: 0.6px; color: var(--silver); margin-top: 2px; }
</style>
</head>
<body>
<main class="canvas">

  <section class="card card--back" aria-label="Card back">
    <ul class="services">
      <li>Staging Houses for Sale</li>
      <li>Minor Home Renovations</li>
      <li>Home Styling &amp; Project Management</li>
      <li>Re-Designing Living Spaces to Aid the Disabled</li>
    </ul>
    <ul class="contact">
      <li><svg viewBox="0 0 12 12"><rect x="3" y="0.5" width="6" height="11" rx="1" fill="var(--gold-light)"/><rect x="4" y="2" width="4" height="6" fill="#111"/></svg>555-014-2290</li>
      <li><svg viewBox="0 0 12 12"><path d="M2 1 L4.5 1 L5.5 3.5 L4 4.8 C5 7 6 8 7.2 8.5 L8.5 7 L11 8 L11 10.5 C6 11 1 6 2 1 Z" fill="var(--gold-light)"/></svg>555-014-3318</li>
      <li><svg viewBox="0 0 12 12"><rect x="1" y="4" width="10" height="6" rx="1" fill="var(--gold-light)"/><rect x="3" y="1" width="6" height="4" fill="var(--gold-light)"/><rect x="3" y="6" width="6" height="1" fill="#111"/></svg>555-014-3375</li>
      <li><svg viewBox="0 0 12 12"><rect x="0.5" y="2" width="11" height="8" rx="1" fill="var(--gold-light)"/><path d="M1 2.5 L6 6.5 L11 2.5" stroke="#111" fill="none"/></svg>info@marenstyling.com</li>
      <li><svg viewBox="0 0 12 12"><circle cx="6" cy="6" r="5" fill="var(--gold-light)"/><path d="M1 6 H11 M6 1 C3 4 3 8 6 11 M6 1 C9 4 9 8 6 11" stroke="#111" stroke-width="0.8" fill="none"/></svg>www.marenstyling.com</li>
      <li><svg viewBox="0 0 12 12"><path d="M6 1 L11.5 6 L10 6 L10 11 L7 11 L7 8 L5 8 L5 11 L2 11 L2 6 L0.5 6 Z" fill="var(--gold-light)"/></svg>214 Larkspur Lane, Ferndale, CO 80611</li>
    </ul>
  </section>

  <section class="card card--front" aria-label="Card front">
    <div class="card__face">
      <div class="wallpaper" role="img" aria-label="Dark French damask wallpaper pattern"></div>
      <p class="tagline">"PROPERTY STYLING AND COSMETIC RENOVATIONS"</p>
      <p class="brand-name">MT Property Styling Pty Ltd</p>
      <div class="holder">
        <p class="holder__name">MAREN TULLOCH B.COM RVA DMH</p>
        <p class="holder__role">PROPERTY STYLIST &amp; PROJECT MANAGER</p>
      </div>
    </div>
  </section>

</main>
</body>
</html>
```